Create our new Brightcup Coffee Syrup Label designs. A delicious job!

Design a front label for a range of coffee syrup flavours. The brand is 'Brightcup Coffee Syrups'. The flavours, vanilla, hazelnut and caramel.
Our coffee syrups are made with only natural colours and flavours and are positioned in the popular premium space in Australian and international cafes.
The labels will be applied to 750 ml Boston Bottles (see attached image).
Given that coffee syrups are often positioned in high visibility locations in cafes, they can be considered as objects of functional beauty.
This range is a sub brand for our company and I have attached our main brand images in the flavours we want. we want this brand to look different to this Marlowe branded range, but included the image to show what we are currently doing in this space.
The different flavours can be identified by a combination of colour and text, which may be a line or section of the otherwise same overall design.
We are going to do a 2 part label with the front just carrying Brand and flavour descriptors plus 750 ml.
Total Bottle height is 240 mm bottle width is 70 mm

Target Market(s)

Cafe patrons, primarily women, 18-35, Middle class in terms of economics, regular cafe patrons. Who are looking for a guilt free treat in their busy day.

Logo Text

Brightcup Coffee Syrups Vanilla (or Hazelnut, or Caramel) 750 ml

Logo styles of interest
Pictorial/Combination Logo
Font styles to use
Sans Serif

Colors

Designer to choose colors to be used in the design.

Requirements
Must have
• A clear design, which is a combination of font and image. it needs to be legible from up to 2m away (across a counter in a cafe).
• We would like to see a device, which may be a gold drop, that may be the 'brightcup' meant to the coffee.
• The way our coffee syrups are used is by adding a small amount (15 ml) to a cup
• of coffee, this adds both flavour and sweetness to the overall coffee experience, and cafes charge a premium for this service. We want our package to show this will be a great thing to do.
• We have a few options in terms of Label stock. We can print on a foil, that will allow a metallic sheen to come through the colours (see example of the Marlowe branded bottles.
Nice to have
• We are looking for a modern, clean and distinctive look and feel to this range.
• I have added a key line for the front and back label, however we can create a different label die line should the design warrant that. Note this is just for the front label.
Should not have
• Difficult to read fonts or imagery that is not clear.
• Should look different to the Marlowe branded product range.

```html
<!DOCTYPE html>
<html lang="en">
<head>
<meta charset="utf-8">
<title>Brightcup Coffee Syrup Labels</title>
<link rel="stylesheet" href="https://fonts.googleapis.com/css2?family=Big+Shoulders+Display:wght@500&family=Josefin+Slab:wght@600&display=swap">
<style>
  :root {
    --canvas: #000000;
    --ink-light: #ffffff;
    --ink-dark: #000000;
    --hazelnut: #e6a98c;
    --vanilla: #f7a21b;
    --caramel: #f0562a;
  }
  * { margin: 0; padding: 0; box-sizing: border-box; }
  html, body {
    width: 1200px;
    height: 1200px;
    overflow: hidden;
    background: var(--canvas);
  }
  .label-range {
    width: 1200px;
    height: 1200px;
    display: flex;
    align-items: center;
    justify-content: center;
    gap: 40px;
  }
  .flavour-label {
    width: 350px;
    height: 444px;
    display: block;
  }
  .flavour-label--hazelnut { --accent: var(--hazelnut); }
  .flavour-label--vanilla  { --accent: var(--vanilla); }
  .flavour-label--caramel  { --accent: var(--caramel); }
  .label-frame {
    fill: none;
    stroke: var(--accent);
    stroke-width: 8;
    stroke-linejoin: round;
    stroke-linecap: round;
  }
  .brand-name {
    font-family: "Big Shoulders Display", sans-serif;
    font-weight: 500;
    font-size: 64px;
    fill: var(--ink-light);
  }
  .syrup-drop { fill: var(--accent); }
  .flavour-name {
    font-family: "Big Shoulders Display", sans-serif;
    font-weight: 500;
    font-size: 44px;
    fill: var(--ink-dark);
  }
  .product-line {
    font-family: "Josefin Slab", serif;
    font-weight: 600;
    font-size: 19px;
    letter-spacing: 6px;
    fill: var(--ink-light);
  }
  .side-dot { fill: var(--accent); }
</style>
</head>
<body>
<main class="label-range">

  <svg class="flavour-label flavour-label--hazelnut" viewBox="0 0 260 330" aria-label="Brightcup Hazelnut Coffee Syrup label">
    <defs>
      <path id="arc-hazelnut" d="M 36 200 A 94 94 0 0 0 224 200"/>
    </defs>
    <path class="label-frame" d="M 28 50 H 10 V 322 H 250 V 50 H 232"/>
    <text class="brand-name" x="130" y="72" text-anchor="middle" textLength="196" lengthAdjust="spacingAndGlyphs">BRIGHTCUP</text>
    <circle class="syrup-drop" cx="130" cy="200" r="68" role="img" aria-label="Golden syrup drop falling into coffee with bubbles"/>
    <text class="flavour-name" x="130" y="215" text-anchor="middle" textLength="108" lengthAdjust="spacingAndGlyphs">HAZELNUT</text>
    <circle class="side-dot" cx="36" cy="176" r="4"/>
    <circle class="side-dot" cx="224" cy="176" r="4"/>
    <text class="product-line"><textPath href="#arc-hazelnut" startOffset="50%" text-anchor="middle">COFFEE • SYRUP</textPath></text>
  </svg>

  <svg class="flavour-label flavour-label--vanilla" viewBox="0 0 260 330" aria-label="Brightcup Vanilla Coffee Syrup label">
    <defs>
      <path id="arc-vanilla" d="M 36 200 A 94 94 0 0 0 224 200"/>
    </defs>
    <path class="label-frame" d="M 28 50 H 10 V 322 H 250 V 50 H 232"/>
    <text class="brand-name" x="130" y="72" text-anchor="middle" textLength="196" lengthAdjust="spacingAndGlyphs">BRIGHTCUP</text>
    <circle class="syrup-drop" cx="130" cy="200" r="68" role="img" aria-label="Golden syrup drop falling into coffee with bubbles"/>
    <text class="flavour-name" x="130" y="215" text-anchor="middle" textLength="96" lengthAdjust="spacingAndGlyphs">VANILLA</text>
    <circle class="side-dot" cx="36" cy="176" r="4"/>
    <circle class="side-dot" cx="224" cy="176" r="4"/>
    <text class="product-line"><textPath href="#arc-vanilla" startOffset="50%" text-anchor="middle">COFFEE • SYRUP</textPath></text>
  </svg>

  <svg class="flavour-label flavour-label--caramel" viewBox="0 0 260 330" aria-label="Brightcup Caramel Coffee Syrup label">
    <defs>
      <path id="arc-caramel" d="M 36 200 A 94 94 0 0 0 224 200"/>
    </defs>
    <path class="label-frame" d="M 28 50 H 10 V 322 H 250 V 50 H 232"/>
    <text class="brand-name" x="130" y="72" text-anchor="middle" textLength="196" lengthAdjust="spacingAndGlyphs">BRIGHTCUP</text>
    <circle class="syrup-drop" cx="130" cy="200" r="68" role="img" aria-label="Golden syrup drop falling into coffee with bubbles"/>
    <text class="flavour-name" x="130" y="215" text-anchor="middle" textLength="100" lengthAdjust="spacingAndGlyphs">CARAMEL</text>
    <circle class="side-dot" cx="36" cy="176" r="4"/>
    <circle class="side-dot" cx="224" cy="176" r="4"/>
    <text class="product-line"><textPath href="#arc-caramel" startOffset="50%" text-anchor="middle">COFFEE • SYRUP</textPath></text>
  </svg>

</main>
</body>
</html>
```